New Television Homescreen Template

We need a new default homescreen design for our televisions. This should reflect our company branding. My company is called Wellward Systems, WSY for short. Our website is www.wsyq.com. We develop televisions and infotainment solutions for the healthcare industry. I am somewhat open to different color palettes but our company colors are blue, black, and white. Our design is constrained by the 9 buttons, however the design of the buttons can be changed. Also, there is a video box on the right side of the screen as shown, this design can also be changed.

Target Market(s)

Hospital Patients

Requirements
Must have
• PSD template.

```html
<!DOCTYPE html>
<html lang="en">
<head>
<meta charset="utf-8">
<title>Wellward Systems – Television Homescreen</title>
<link rel="stylesheet" href="https://fonts.googleapis.com/css2?family=Roboto+Condensed:wght@700&family=Arimo:ital,wght@0,400;1,400&display=swap">
<style>
  :root {
    --page: #ffffff;
    --header: #2f2f2f;
    --brand-blue: #5cc3ee;
    --brand-text: #ffffff;
    --room-light: #f3f5f6;
    --room-mid: #dfe3e5;
    --room-deep: #c9ced1;
    --tile-frame: #e9ebec;
    --tile-frame-edge: #c4c8ca;
    --tile-top: #66c4ee;
    --tile-bottom: #3f94c4;
    --tile-text: #ffffff;
    --player-frame: #9d9d9d;
    --player-screen: #3a3a3a;
    --player-bar: #222222;
    --footer-band: #555555;
    --footer-text: #ffffff;
  }
  * { box-sizing: border-box; margin: 0; padding: 0; }
  html, body { width: 1200px; height: 1000px; overflow: hidden; background: var(--page); }
  .canvas { position: relative; width: 1200px; height: 1000px; }

  .homescreen { position: absolute; left: 0; top: 167px; width: 1200px; height: 675px; overflow: hidden; }

  .top-bar { position: absolute; left: 0; top: 0; width: 100%; height: 93px; background: var(--header); }
  .brand { position: absolute; right: 65px; top: 0; height: 93px; display: flex; align-items: center; gap: 12px; }
  .brand-mark { width: 14px; height: 14px; background: var(--brand-blue); }
  .brand-name { font-family: "Arimo", sans-serif; font-weight: 400; font-size: 26px; line-height: 30px; color: var(--brand-text); }

  .room-backdrop { position: absolute; left: 0; top: 93px; width: 100%; height: 582px;
    background: linear-gradient(90deg, var(--room-light) 0%, var(--room-mid) 45%, var(--room-light) 62%, var(--room-mid) 82%, var(--room-deep) 100%); }

  .channel-grid { position: absolute; left: 68px; top: 114px; width: 582px; height: 490px; }
  .channel-tile { position: absolute; width: 150px; height: 150px; border-radius: 10px;
    background: var(--tile-frame); border: 1px solid var(--tile-frame-edge);
    box-shadow: 0 1px 3px rgba(0,0,0,0.15); }
  .channel-tile .face { position: absolute; inset: 7px; border-radius: 8px;
    background: linear-gradient(180deg, var(--tile-top) 0%, #58b3e0 50%, var(--tile-bottom) 100%);
    display: flex; align-items: center; justify-content: center;
    font-family: "Roboto Condensed", sans-serif; font-weight: 700; font-size: 28px;
    color: var(--tile-text); text-shadow: 0 2px 3px rgba(0,0,0,0.45); letter-spacing: -0.6px; white-space: nowrap; }
  .c1 { left: 0; } .c2 { left: 220px; } .c3 { left: 431px; }
  .r1 { top: 0; } .r2 { top: 171px; } .r3 { top: 339px; }

  .video-player { position: absolute; left: 767px; top: 112px; width: 374px; height: 224px;
    background: var(--player-frame); border-radius: 6px; }
  .video-screen { position: absolute; left: 25px; top: 7px; width: 322px; height: 190px;
    background: radial-gradient(ellipse at 50% 45%, #4a4a4a 0%, var(--player-screen) 70%, #2a2a2a 100%); }
  .play-button { position: absolute; left: 95px; top: 31px; }
  .video-controls { position: absolute; left: 12px; top: 196px; width: 350px; height: 20px;
    background: var(--player-bar); border-radius: 2px; }
  .video-controls svg { display: block; }

  .patient-photo { position: absolute; left: 765px; top: 358px; width: 350px; height: 317px;
    background: linear-gradient(180deg, rgba(234,214,200,0.0) 0%, #e7cbb8 30%, #b9cde6 70%, #a9c1e0 100%);
    border-radius: 140px 140px 0 0; }

  .footer-band { position: absolute; left: 0; top: 633px; width: 800px; height: 42px;
    background: linear-gradient(90deg, var(--footer-band) 0%, var(--footer-band) 80%, rgba(85,85,85,0.6) 100%); }
  .footer-text { position: absolute; left: 53px; top: 7px; font-family: "Arimo", sans-serif; font-style: italic;
    font-size: 22px; line-height: 28px; color: var(--footer-text); white-space: nowrap; }
</style>
</head>
<body>
<div class="canvas">
  <main class="homescreen">
    <header class="top-bar">
      <div class="brand">
        <span class="brand-mark" aria-hidden="true"></span>
        <span class="brand-name">Wellward Systems</span>
      </div>
    </header>

    <div class="room-backdrop" role="img" aria-label="Softly blurred bright hospital room with a bed and window"></div>

    <nav class="channel-grid" aria-label="Channels">
      <a class="channel-tile c1 r1"><span class="face">Cable TV</span></a>
      <a class="channel-tile c2 r1"><span class="face">Cable TV</span></a>
      <a class="channel-tile c3 r1"><span class="face">Cable TV</span></a>
      <a class="channel-tile c1 r2"><span class="face">Cable TV</span></a>
      <a class="channel-tile c2 r2"><span class="face">Cable TV</span></a>
      <a class="channel-tile c3 r2"><span class="face">Cable TV</span></a>
      <a class="channel-tile c1 r3"><span class="face">Cable TV</span></a>
      <a class="channel-tile c2 r3"><span class="face">Cable TV</span></a>
      <a class="channel-tile c3 r3"><span class="face">Cable TV</span></a>
    </nav>

    <section class="video-player" aria-label="Featured video">
      <div class="video-screen" role="img" aria-label="Video still frame on a dark background">
        <svg class="play-button" width="128" height="128" viewBox="0 0 128 128" aria-hidden="true">
          <circle cx="64" cy="64" r="62" fill="rgba(200,200,200,0.55)" stroke="rgba(230,230,230,0.6)" stroke-width="3"/>
          <polygon points="50,38 50,90 92,64" fill="rgba(60,60,60,0.75)"/>
        </svg>
      </div>
      <div class="video-controls">
        <svg width="350" height="20" viewBox="0 0 350 20" aria-hidden="true">
          <polygon points="11,4 11,16 21,10" fill="#ffffff"/>
          <rect x="30" y="8" width="262" height="4" rx="2" fill="#555555"/>
          <circle cx="36" cy="10" r="5" fill="#ffffff"/>
          <text x="301" y="14" font-family="Arimo, sans-serif" font-size="10" fill="#ffffff">0:00</text>
          <path d="M329 15 L339 5 M333 15 L339 9 M337 15 L339 13" stroke="#bbbbbb" stroke-width="1.5"/>
        </svg>
      </div>
    </section>

    <div class="patient-photo" role="img" aria-label="Smiling elderly patient in pale blue pyjamas with a caring nurse behind him"></div>

    <footer class="footer-band">
      <p class="footer-text">Creating tools to improve the health of our country and world.</p>
    </footer>
  </main>
</div>
</body>
</html>
```